Law Office Business Card

We need a business card design to include the following information:
Name of Firm: Brennick Law Group, P.A.
Address: 4627 Sandlot Ave, Ste 208, West Palm Beach, FL 33409
Phone: 561-555-0148
Fax: 561-555-0193
Website: http://www.tbrennicklaw.example

We Need a place for the Person's name and email address. Please start with the following:
Lorna K. Dwyer, Esq.
lorna@tbrennicklaw.example

```html
<!DOCTYPE html>
<html lang="en">
<head>
<meta charset="utf-8">
<title>Brennick Law Group – Business Card</title>
<link href="https://fonts.googleapis.com/css2?family=Source+Sans+3:wght@400;600&display=swap" rel="stylesheet">
<style>
  :root {
    --backdrop: #2b2b2c;
    --card: #0d0d0e;
    --card-panel: #141415;
    --gold: #c9ab88;
    --ink: #e9e6e1;
    --frame: #5a5249;
  }
  * { box-sizing: border-box; margin: 0; padding: 0; }
  html, body {
    width: 1200px; height: 900px; overflow: hidden;
    background: var(--backdrop);
    font-family: "Source Sans 3", "Myriad Pro", Arial, sans-serif;
  }
  .stage {
    position: relative; width: 1200px; height: 900px;
    display: flex; align-items: center; justify-content: center; gap: 60px;
  }
  .card {
    position: relative; width: 500px; height: 286px;
    background: var(--card); border-radius: 22px; overflow: hidden;
    box-shadow: 0 10px 30px rgba(0,0,0,.45);
  }
  /* back side: brand + contact */
  .card-back .brand-area {
    position: absolute; left: 0; top: 0; width: 230px; height: 100%;
    display: flex; align-items: center; justify-content: center; gap: 10px;
  }
  .brand-square {
    width: 14px; height: 14px; border: 1.5px solid var(--gold); flex: none;
  }
  .brand-name {
    color: var(--gold); font-weight: 600; font-size: 19px; letter-spacing: .04em;
    text-transform: uppercase; line-height: 1.2;
  }
  .card-back .contact-panel {
    position: absolute; left: 230px; top: 0; right: 0; height: 100%;
    background: var(--card-panel);
    padding: 56px 20px 0 28px; color: var(--ink);
  }
  .person-name {
    color: var(--gold); font-weight: 600; font-size: 17px; margin-bottom: 14px;
  }
  .address { font-size: 13px; line-height: 1.45; margin-bottom: 14px; }
  .contact-list { list-style: none; font-size: 13px; line-height: 1.6; }
  .contact-list li { display: flex; align-items: center; gap: 8px; }
  .contact-list svg { width: 11px; height: 11px; flex: none; fill: var(--gold); }
  /* front side: brand only */
  .card-front {
    display: flex; align-items: center; justify-content: center; gap: 12px;
  }
  .card-front .brand-name { font-size: 28px; }
  .card-front .brand-square { width: 18px; height: 18px; }
</style>
</head>
<body>
<main class="stage">
  <article class="card card-back">
    <div class="brand-area">
      <span class="brand-square"></span>
      <span class="brand-name">Brennick<br>Law Group</span>
    </div>
    <div class="contact-panel">
      <h1 class="person-name">Lorna K. Dwyer, Esq.</h1>
      <p class="address">4627 Sandlot Ave, Ste 208, West<br>Palm Beach, FL 33409</p>
      <ul class="contact-list">
        <li><svg viewBox="0 0 12 12"><path d="M2.5 0.8l2 2.3-1 1.3c.7 1.6 2 2.9 3.6 3.6l1.3-1 2.3 2-1.2 2C5 10.6 1.4 7 .6 2z"/></svg>561-555-0148</li>
        <li><svg viewBox="0 0 12 12"><path d="M3 0h5v3H3zM1 4h10v6H1zM3 8h6v4H3z"/></svg>561-555-0193</li>
        <li><svg viewBox="0 0 12 12"><path d="M0 2h12v8H0zM1 3l5 3.5L11 3v-.2H1z" fill-rule="evenodd"/></svg>lorna@tbrennicklaw.example</li>
        <li><svg viewBox="0 0 12 12"><circle cx="6" cy="6" r="5.5"/></svg>www.tbrennicklaw.example</li>
      </ul>
    </div>
  </article>
  <article class="card card-front">
    <span class="brand-square"></span>
    <span class="brand-name">Brennick Law Group</span>
  </article>
</main>
</body>
</html>
```